Create Social Media design templates for Online-Education-Startup

We are an online platform for pupils who provide group courses and on demand individual tutroing lessons. Our core values are personalisation, family and success. We need a holistic social media design concept which includes nine possible layouts for Instagram posts which reflect our values and promote not only our offerings and special deals but also support in building our brand image (for example: telling company history, daily news, funny facts, getting to know the team etc.).
Additionally, we need design elements for our YouTube channel:
-Videocover
-Cover Image for the channel

Our main colour is orange (RGB-Code: 255;105;31) and additional colours white, black, and grey. For the reference have a look at our website: www.lernquorvo.de.

Target Market(s)

We want to attract customers to our online tutoring courses and build a brand.

Industry/Entity Type

Education / Tutoring

Font styles to use
Sans Serif

Requirements
Must have
• Familiarize yourself with the style of our website. The designs should fit as well as possible.

```html
<!DOCTYPE html>
<html lang="de">
<head>
<meta charset="utf-8">
<title>Lernquorvo – Social Media Templates</title>
<link href="https://fonts.googleapis.com/css2?family=Poppins:wght@400;500;600;700;800&display=swap" rel="stylesheet">
<style>
:root{
  --orange:#ff691f;
  --black:#0d0d0d;
  --white:#ffffff;
  --grey:#e9e9e9;
  --grey-dark:#555;
  --stage:#a9a9a9;
  --photo-warm:linear-gradient(135deg,#c9b8a6,#7d6a5c);
  --photo-cool:linear-gradient(135deg,#dfe4ea,#9aa3ad);
  --photo-blue:linear-gradient(160deg,#6f93d6,#1c2f78);
  --photo-dark:linear-gradient(135deg,#6b5e55,#2d2622);
}
*{margin:0;padding:0;box-sizing:border-box}
html,body{width:1200px;height:1117px;overflow:hidden}
body{background:radial-gradient(ellipse at 50% 40%,#c4c4c4,var(--stage));font-family:"Poppins",sans-serif;color:var(--black);position:relative}
.tile{position:absolute;width:321px;height:321px;background:var(--white);overflow:hidden;box-shadow:0 6px 14px rgba(0,0,0,.25)}
.abs{position:absolute}
.photo{position:absolute}
.brand{position:absolute;display:flex;align-items:center;gap:6px}
.brand-dot{border-radius:50%;background:var(--orange);flex:none}
.brand-name{font-weight:700;line-height:1.1}
.brand-sub{font-weight:400;line-height:1.15}
.label{position:absolute;background:var(--orange);color:var(--white);font-weight:700;display:flex;align-items:center;justify-content:center;border-radius:2px}
.label::after{content:"";position:absolute;bottom:-6px;left:50%;margin-left:-6px;border:6px solid transparent;border-bottom:0;border-top-color:var(--orange)}
.tick{display:inline-block;width:8px;height:8px;border-radius:50%;background:var(--orange);position:relative;flex:none}
.tick::after{content:"";position:absolute;left:2.4px;top:1.4px;width:2px;height:4px;border:solid #fff;border-width:0 1.2px 1.2px 0;transform:rotate(45deg)}
.contact-bar{position:absolute;background:var(--orange);color:var(--white);display:flex;align-items:center;justify-content:center;gap:12px;font-size:8px;border-radius:8px 8px 0 0}
.contact-bar b{font-weight:700}
.ico{display:inline-block;width:7px;height:7px;border-radius:50%;background:currentColor;vertical-align:-1px;margin-right:2px}
.lorem{font-size:7px;line-height:1.25}
</style>
</head>
<body>

<!-- Tile 1: Online-Nachhilfe -->
<section class="tile" style="left:89px;top:54px">
  <div class="photo" role="img" aria-label="Foto: lächelnder Mann im Anzug mit Laptop, Daumen hoch" style="left:170px;top:20px;width:151px;height:301px;background:linear-gradient(160deg,#e7dcd2,#2a3f7a 60%,#18275a)"></div>
  <div class="brand" style="left:16px;top:18px">
    <span class="brand-dot" style="width:52px;height:52px"></span>
    <div><div class="brand-name" style="font-size:19px">Lernquorvo</div><div class="brand-sub" style="font-size:17px">Bildungsinstitut</div></div>
  </div>
  <div class="abs" style="left:21px;top:92px;width:190px;height:102px;background:var(--orange);border-radius:8px;color:#fff;padding:8px 14px">
    <div style="font-size:17px;font-weight:700;line-height:1.12">Online-Nachhilfe<br>bei Lernquorvo</div>
    <div style="width:44px;height:1px;background:#fff;margin:3px 0 6px"></div>
    <div style="font-size:9.5px;line-height:1.05">Gemeinsam für Deinen<br>Abschluss!</div>
    <div style="font-size:5px;margin-top:2px">persönlich • familiär •<br>erfolgreich.</div>
  </div>
  <div class="abs" style="left:35px;top:204px;font-size:10px;font-weight:600;line-height:1.05">
    <div style="display:flex;gap:4px"><span class="tick" style="margin-top:2px"></span><span>vollständig<br>flexibel</span></div>
    <div style="display:flex;gap:4px;margin-top:10px"><span class="tick" style="margin-top:2px"></span><span>Kein Abo</span></div>
  </div>
  <svg class="abs" style="left:0;top:240px" width="321" height="81" viewBox="0 0 321 81">
    <path d="M0 22 Q120 10 230 0 L321 0 L321 81 L0 81Z" fill="var(--orange)"/>
    <path d="M0 35 Q120 22 240 12 L321 10 L321 81 L0 81Z" fill="var(--black)"/>
  </svg>
  <div class="abs" style="left:89px;top:274px;width:14px;height:14px;border-radius:50%;background:var(--orange)"></div>
  <div class="abs" style="left:35px;top:292px;color:#fff;font-size:12px;font-weight:700">www.lernquorvo.de</div>
</section>

<!-- Tile 2: Core values -->
<section class="tile" style="left:433px;top:54px">
  <div class="photo" role="img" aria-label="Foto: Gruppe junger Leute im hellen Büro, einer hebt den Arm" style="left:175px;top:0;width:146px;height:321px;background:var(--photo-cool);border-radius:120px 0 0 0"></div>
  <svg class="abs" style="left:180px;top:0" width="141" height="40"><path d="M0 0 L141 0 L141 2 Q70 20 30 35Z" fill="var(--black)"/></svg>
  <div class="abs" style="left:29px;top:24px;font-size:25px;font-weight:800;line-height:1">OUR CORE</div>
  <div class="label" style="left:28px;top:52px;width:131px;height:29px;font-size:24px;font-weight:800">VALUES</div>
  <div class="abs" style="left:28px;top:96px;width:163px;height:103px;background:#fff;border:2px solid var(--grey);border-radius:8px;padding:10px 10px;font-size:15.5px;font-weight:700">
    <div style="display:flex;align-items:center;gap:5px"><span class="tick"></span>personalisation</div>
    <div style="display:flex;align-items:center;gap:5px;margin-top:8px"><span class="tick"></span>family and</div>
    <div style="display:flex;align-items:center;gap:5px;margin-top:8px"><span class="tick"></span>success.</div>
  </div>
  <div class="abs brand-dot" style="left:57px;top:210px;width:50px;height:50px"></div>
  <div class="abs" style="left:32px;top:260px"><div class="brand-name" style="font-size:15px">Lernquorvo</div><div class="brand-sub" style="font-size:13.5px">Bildungsinstitut</div></div>
  <svg class="abs" style="left:140px;top:230px" width="181" height="91"><path d="M0 91 Q30 5 181 0 L181 91Z" fill="var(--orange)"/></svg>
  <div class="abs" style="right:21px;top:248px;color:#fff;text-align:right;line-height:1.15">
    <div style="font-size:8px">Telepon:</div><div style="font-size:10px;font-weight:700"><span class="ico"></span>089 55501234</div>
    <div style="font-size:8px;margin-top:4px">Website:</div><div style="font-size:10px;font-weight:700"><span class="ico"></span>www.lernquorvo.de</div>
  </div>
</section>

<!-- Tile 3: Unser Team -->
<section class="tile" style="left:776px;top:54px">
  <div class="label" style="left:29px;top:28px;width:131px;height:27px;font-size:19px">Unser Team</div>
  <div class="brand" style="left:186px;top:20px;gap:4px">
    <span class="brand-dot" style="width:34px;height:34px"></span>
    <div><div class="brand-name" style="font-size:10.5px">Lernquorvo</div><div class="brand-sub" style="font-size:9px">Bildungsinstitut</div></div>
  </div>
  <p class="abs" style="left:28px;top:71px;width:262px;font-size:8.3px;line-height:1.3">Die Trainer bei Lernquorvo bieten Begeisterung und Professionalität. Unser Qualitätsanspruch unterscheidet uns von anderen Angeboten.</p>
  <div class="photo" role="img" aria-label="Foto: lächelnde Teilnehmer in einem Seminarraum" style="left:0;top:142px;width:321px;height:179px;background:var(--photo-warm);border-radius:60px 0 0 0"></div>
  <svg class="abs" style="left:0;top:165px" width="55" height="60"><path d="M0 0 L52 25 L0 58Z" fill="var(--black)"/></svg>
  <div class="abs" style="left:28px;top:110px;width:263px;height:37px;background:#fff;border:1.5px solid var(--orange);border-radius:5px;display:flex;align-items:center;justify-content:space-around;font-size:7.5px;font-weight:600;line-height:1.2">
    <div style="display:flex;gap:4px;align-items:center"><span class="tick" style="width:20px;height:20px"></span>Zeitliche<br>Flexibilität</div>
    <div style="display:flex;gap:4px;align-items:center"><span class="tick" style="width:20px;height:20px"></span>Online-<br>Unterricht</div>
    <div style="display:flex;gap:4px;align-items:center"><span class="tick" style="width:20px;height:20px"></span>Mitarbeiter-<br>Schulung</div>
  </div>
  <div class="contact-bar" style="left:22px;top:288px;width:278px;height:33px"><span>Telepon: <b><span class="ico"></span>089 55501234</b></span><span>Website: <b><span class="ico"></span>www.lernquorvo.de</b></span></div>
</section>

<!-- Tile 4: Company History -->
<section class="tile" style="left:89px;top:393px">
  <div class="photo" role="img" aria-label="Foto: Publikum im Hörsaal, Redner vorne" style="left:100px;top:0;width:221px;height:230px;background:var(--photo-cool)"></div>
  <div class="photo" role="img" aria-label="Foto: Seminarraum am linken Rand" style="left:0;top:0;width:20px;height:180px;background:var(--photo-warm)"></div>
  <svg class="abs" style="left:170px;top:200px" width="151" height="50"><path d="M0 30 Q80 0 151 20 L151 50 L0 50Z" fill="#fff"/></svg>
  <div class="abs" style="left:17px;top:0;width:160px;height:254px;background:var(--orange);border-radius:0 0 10px 10px;color:#fff;padding:14px 17px">
    <div style="font-size:19px;font-weight:700;line-height:1.05">Company<br>History</div>
    <div style="width:36px;height:1.5px;background:#fff;margin:3px 0 9px"></div>
    <p class="lorem" style="font-size:6.9px;line-height:1.18">Lorem ipsum dolor sit amet, consectetur adipiscing elit, sed do eiusmod tempor incididunt ut labore et dolore magnaaliqua. Ut enim ad minim veniam, quis nostrud exercitation ullamco laboris nisi ut aliquip ex ea commodo consequat. Duis aute irure dolor in reprehenderit in voluptate velit esse cillum dolore eu fugiat nulla pariatur.</p>
    <p class="lorem" style="font-size:6.9px;line-height:1.18;margin-top:6px">Excepteur sint occaecat cupidatat non proident, sunt in culpa qui officia deserunt mollit anim id est laborum.</p>
    <p class="lorem" style="font-size:6.9px;line-height:1.18;margin-top:6px">Lorem ipsum dolor sit amet, consectetur adipiscing elit, sed do eiusmod tempor incididunt ut labore et dolore magnaaliqua.</p>
  </div>
  <div class="brand" style="left:26px;top:266px;gap:5px">
    <span class="brand-dot" style="width:36px;height:36px"></span>
    <div><div class="brand-name" style="font-size:11.5px">Lernquorvo</div><div class="brand-sub" style="font-size:10.5px">Bildungsinstitut</div></div>
  </div>
  <svg class="abs" style="left:150px;top:238px" width="171" height="83"><path d="M0 83 Q40 5 171 0 L171 83Z" fill="var(--black)"/></svg>
  <div class="abs" style="right:22px;top:255px;color:#fff;text-align:right;line-height:1.15">
    <div style="font-size:8px">Telepon:</div><div style="font-size:10px;font-weight:700"><span class="ico" style="color:var(--orange)"></span>089 55501234</div>
    <div style="font-size:8px;margin-top:3px">Website:</div><div style="font-size:10px;font-weight:700"><span class="ico" style="color:var(--orange)"></span>www.lernquorvo.de</div>
  </div>
</section>

<!-- Tile 5: Daily News -->
<section class="tile" style="left:433px;top:393px">
  <div class="label" style="left:27px;top:19px;width:132px;height:27px;font-size:17px">Daily News</div>
  <div class="brand" style="left:190px;top:20px;gap:4px">
    <span class="brand-dot" style="width:34px;height:34px"></span>
    <div><div class="brand-name" style="font-size:10.5px">Lernquorvo</div><div class="brand-sub" style="font-size:9px">Bildungsinstitut</div></div>
  </div>
  <p class="abs lorem" style="left:27px;top:58px;width:150px;font-size:7.2px;line-height:1.2">Lorem ipsum dolor sit amet, consectetur adipiscing elit, sed do eiusmod tempor incididunt ut labore et dolore magna aliqua. Ut enim ad minim veniam, quis nostrud exercitation ullamco laboris nisi ut aliquip ex ea commodo consequat. Duis aute irure dolor in reprehenderit in voluptate velit esse cillum dolore eu fugiat nulla pariatur.</p>
  <div class="photo" role="img" aria-label="Foto: moderne Glasfassade eines Bürogebäudes" style="left:187px;top:60px;width:134px;height:157px;background:var(--photo-blue);border-radius:10px 0 0 0"></div>
  <div class="photo" role="img" aria-label="Foto: zwei Personen arbeiten am Laptop" style="left:27px;top:150px;width:120px;height:120px;background:var(--photo-cool);border-radius:8px 0 0 8px"></div>
  <div class="abs" style="left:129px;top:150px;width:164px;height:120px;background:#fff;border:1.5px solid var(--orange);border-radius:8px;padding:7px 8px;font-size:5.8px;line-height:1.2">
    <div style="display:flex;gap:4px"><span class="tick" style="width:6px;height:6px"></span><span>Lorem ipsum dolor sit amet, consectetur adipiscing elit, sed do eiusmod tempor incididunt ut labore et dolore magna aliqua.</span></div>
    <div style="display:flex;gap:4px;margin-top:8px"><span class="tick" style="width:6px;height:6px"></span><span>Lorem ipsum dolor sit amet, consectetur adipiscing elit, sed do eiusmod tempor incididunt ut labore et dolore magna aliqua.</span></div>
    <div style="display:flex;gap:4px;margin-top:8px"><span class="tick" style="width:6px;height:6px"></span><span>Lorem ipsum dolor sit amet, consectetur adipiscing elit, sed do eiusmod tempor incididunt ut labore et dolore magna aliqua.</span></div>
  </div>
  <div class="contact-bar" style="left:22px;top:286px;width:278px;height:35px"><span>Telepon: <b><span class="ico"></span>089 55501234</b></span><span>Website: <b><span class="ico"></span>www.lernquorvo.de</b></span></div>
</section>

<!-- Tile 6: funny facts -->
<section class="tile" style="left:776px;top:393px">
  <div class="label" style="left:25px;top:19px;width:132px;height:27px;font-size:17px">funny facts</div>
  <div class="brand" style="left:189px;top:20px;gap:4px">
    <span class="brand-dot" style="width:34px;height:34px"></span>
    <div><div class="brand-name" style="font-size:10.5px">Lernquorvo</div><div class="brand-sub" style="font-size:9px">Bildungsinstitut</div></div>
  </div>
  <div class="abs" style="left:25px;top:63px;width:271px;display:grid;grid-template-columns:132px 132px;gap:6px 7px;font-size:5.8px;line-height:1.2">
    <div style="background:var(--grey);border-radius:5px;padding:7px 7px;display:flex;gap:4px;height:43px"><span class="tick" style="width:6px;height:6px"></span><span>Lorem ipsum dolor sit amet, consectetur adipiscing elit, sed do eiusmod tempor incididunt ut labore et dolore magna aliqua.</span></div>
    <div style="padding:7px 7px;display:flex;gap:4px;height:43px"><span class="tick" style="width:6px;height:6px"></span><span>Lorem ipsum dolor sit amet, consectetur adipiscing elit, sed do eiusmod tempor incididunt ut labore et dolore magna aliqua.</span></div>
    <div style="padding:7px 7px;display:flex;gap:4px;height:43px"><span class="tick" style="width:6px;height:6px"></span><span>Lorem ipsum dolor sit amet, consectetur adipiscing elit, sed do eiusmod tempor incididunt ut labore et dolore magna aliqua.</span></div>
    <div style="background:var(--grey);border-radius:5px;padding:7px 7px;display:flex;gap:4px;height:43px"><span class="tick" style="width:6px;height:6px"></span><span>Lorem ipsum dolor sit amet, consectetur adipiscing elit, sed do eiusmod tempor incididunt ut labore et dolore magna aliqua.</span></div>
    <div style="background:var(--grey);border-radius:5px;padding:7px 7px;display:flex;gap:4px;height:43px"><span class="tick" style="width:6px;height:6px"></span><span>Lorem ipsum dolor sit amet, consectetur adipiscing elit, sed do eiusmod tempor incididunt ut labore et dolore magna aliqua.</span></div>
    <div style="padding:7px 7px;display:flex;gap:4px;height:43px"><span class="tick" style="width:6px;height:6px"></span><span>Lorem ipsum dolor sit amet, consectetur adipiscing elit, sed do eiusmod tempor incididunt ut labore et dolore magna aliqua.</span></div>
  </div>
  <div class="photo" role="img" aria-label="Foto: Hände arbeiten an Plänen mit Windrad-Modell auf dem Tisch" style="left:0;top:218px;width:321px;height:103px;background:var(--photo-dark)"></div>
</section>

<!-- Tile 7: Lorem ipsum group -->
<section class="tile" style="left:89px;top:732px">
  <div class="abs" style="left:10px;top:18px;width:155px;text-align:center">
    <div style="font-size:18px;font-weight:700;line-height:1">Lorem <span style="color:var(--orange)">ipsum</span></div>
    <div style="font-size:10.5px;font-weight:500;line-height:1.15;margin-top:3px">Lorem ipsum dolor<br>sit amet, consectetur<br>adipiscing elit,</div>
  </div>
  <div class="brand" style="left:168px;top:26px;gap:5px">
    <span class="brand-dot" style="width:44px;height:44px"></span>
    <div><div class="brand-name" style="font-size:12px">Lernquorvo</div><div class="brand-sub" style="font-size:11px">Bildungsinstitut</div></div>
  </div>
  <div class="abs lorem" style="left:19px;top:86px;width:283px;height:56px;border:1.5px solid var(--orange);border-radius:6px;padding:7px 12px;font-size:6.3px;line-height:1.22;text-align:center">Lorem ipsum dolor sit amet, consectetur adipiscing elit, sed do eiusmod tempor incididunt ut labore et dolore magnaaliqua. Ut enim ad minim veniam, quis nostrud exercitation ullamco laboris nisi ut aliquip ex ea commodo consequat. Duis aute irure dolor in reprehenderit in voluptate velit esse cillum dolore eu fugiat nulla pariatur.</div>
  <div class="abs" style="left:0;top:262px;width:321px;height:59px;background:var(--black)"></div>
  <div class="photo" role="img" aria-label="Foto: Gruppe von Menschen im hellen Foyer" style="left:17px;top:148px;width:287px;height:135px;background:var(--photo-warm);border:3px solid #fff;border-radius:10px"></div>
  <div class="abs" style="left:0;top:300px;width:321px;display:flex;justify-content:center;gap:12px;color:#fff;font-size:7.5px"><span>Telepon: <b><span class="ico"></span>089 55501234</b></span><span>Website: <b><span class="ico"></span>www.lernquorvo.de</b></span></div>
</section>

<!-- Tile 8: Lorem ipsum dolor -->
<section class="tile" style="left:433px;top:732px">
  <div class="photo" role="img" aria-label="Foto: Frau präsentiert vor Zuhörern im Konferenzraum" style="left:150px;top:0;width:171px;height:321px;background:var(--photo-cool);clip-path:polygon(55% 0,100% 0,100% 100%,0 100%)"></div>
  <svg class="abs" style="left:0;top:0" width="321" height="321"><path d="M236 0 L246 0 L147 321 L137 321Z" fill="var(--orange)"/></svg>
  <div class="brand" style="left:26px;top:20px;gap:5px">
    <span class="brand-dot" style="width:38px;height:38px"></span>
    <div><div class="brand-name" style="font-size:12px">Lernquorvo</div><div class="brand-sub" style="font-size:11px">Bildungsinstitut</div></div>
  </div>
  <div class="abs" style="left:26px;top:70px;font-size:19px;font-weight:800;line-height:1">LOREM<br><span style="color:var(--orange)">IPSUM DOLOR<br>SIT AMET</span></div>
  <div class="abs" style="left:26px;top:133px;font-size:9px;font-weight:600;line-height:1.15">Lorem ipsum dolor sit amet,<br>fugiat nulla pariatur.</div>
  <div class="abs" style="left:26px;top:158px;width:52px;height:1.5px;background:var(--orange)"></div>
  <p class="abs" style="left:26px;top:169px;width:125px;font-size:7.8px;line-height:1.25">Lorem ipsum dolor sit amet, consectetur adipiscing elit, sed do eiusmod tempor incididunt ut labore et dolore magnaaliqua. Ut enim ad minim veniam, quis nostrud exercitation ullamco laboris nisi ut aliquip ex ea commodo consequat.</p>
  <svg class="abs" style="left:0;top:273px" width="160" height="48"><path d="M0 0 L160 0 L145 48 L0 48Z" fill="var(--black)"/></svg>
  <div class="abs" style="left:26px;top:287px;color:#fff;line-height:1.2"><div style="font-size:7px">Website:</div><div style="font-size:8.5px;font-weight:700"><span class="ico" style="color:var(--orange)"></span>www.lernquorvo.de</div></div>
</section>

<!-- Tile 9: Lorem ipsum orange -->
<section class="tile" style="left:776px;top:732px">
  <svg class="abs" style="left:0;top:0" width="321" height="150"><path d="M0 0 L321 0 L321 140 Q160 110 0 140Z" fill="var(--orange)"/></svg>
  <div class="abs" style="left:0;top:26px;width:321px;text-align:center;color:#fff">
    <div style="font-size:17px;font-weight:700;line-height:1.05">Lorem ipsum dolor sit amet,<br>consectetur adipiscing elit</div>
    <p style="font-size:6.3px;line-height:1.22;margin:7px auto 0;width:260px">Lorem ipsum dolor sit amet, consectetur adipiscing elit, sed do eiusmod tempor incididunt ut labore et dolore magnaaliqua. Ut enim ad minim veniam, quis nostrud exercitation ullamco laboris nisi ut aliquip ex ea commodo consequat. Duis aute irure dolor in reprehenderit in voluptate velit esse cillum dolore eu fugiat nulla pariatur.</p>
  </div>
  <div class="abs" style="left:24px;top:122px;width:272px;height:109px;background:#fff;border-radius:8px"></div>
  <div class="photo" role="img" aria-label="Foto: Mädchen mit Kopfhörern winkt vor dem Laptop" style="left:27px;top:125px;width:88px;height:103px;background:var(--photo-cool);border-radius:6px"></div>
  <div class="photo" role="img" aria-label="Foto: Schülerin lernt am Laptop" style="left:117px;top:125px;width:88px;height:103px;background:var(--photo-warm);border-radius:6px"></div>
  <div class="photo" role="img" aria-label="Foto: Junge beim Online-Unterricht am Schreibtisch" style="left:207px;top:125px;width:87px;height:103px;background:var(--photo-dark);border-radius:6px"></div>
  <div class="brand" style="left:46px;top:238px;gap:10px">
    <span class="brand-dot" style="width:66px;height:66px"></span>
    <div><div class="brand-name" style="font-size:22px">Lernquorvo</div><div class="brand-sub" style="font-size:20px">Bildungsinstitut</div></div>
  </div>
</section>

</body>
</html>
```